Business Card - HOBEL

We need business cards for our dog rescue... we have a wonderful logo which I am including. The front of the card should show our contact information and our logo. The back should show our two dog adoption site addresses:

www.KennoLoop.com/shelter40391-pets.html
www.tailwick.com/shelters/vq216.html

```html
<!DOCTYPE html>
<html lang="en">
<head>
<meta charset="utf-8">
<title>HOBEL Business Card</title>
<link rel="stylesheet" href="https://fonts.googleapis.com/css2?family=Righteous&display=swap">
<style>
  :root {
    --page: #e3e3e1;
    --card: #ffffff;
    --green: #0f6e37;
    --blue: #3a4fa6;
    --red: #ec1c24;
    --paw: #c9cbe6;
    --ink-green: #0f6e37;
  }
  * { box-sizing: border-box; margin: 0; padding: 0; }
  html, body {
    width: 1200px; height: 928px; overflow: hidden;
    background: var(--page);
    font-family: "Righteous", "Trebuchet MS", sans-serif;
  }
  .card {
    position: absolute; left: 260px;
    width: 680px; height: 389px;
    background: var(--card);
    box-shadow: 0 6px 18px rgba(0,0,0,.18);
    overflow: hidden;
  }
  .card--back { top: 50px; }
  .card--front { top: 489px; }
  .card__art { position: absolute; inset: 0; width: 680px; height: 389px; }

  /* back */
  .back__name { position: absolute; top: 100px; width: 100%; text-align: center; color: var(--red); font-size: 22px; }
  .back__tagline { position: absolute; top: 128px; width: 100%; text-align: center; color: var(--ink-green); font-size: 22px; }
  .back__label { position: absolute; top: 218px; width: 100%; text-align: center; color: var(--red); font-size: 20px; }
  .back__url {
    position: absolute; left: 122px; width: 440px; height: 26px;
    background: var(--blue); color: #fff; font-size: 15px;
    display: flex; align-items: center; justify-content: center; letter-spacing: .3px;
  }
  .back__url--one { top: 250px; }
  .back__url--two { top: 284px; }

  /* front */
  .brand {
    position: absolute; left: 40px; top: 110px; width: 220px; height: 130px;
    display: flex; align-items: center; gap: 12px;
  }
  .brand__mark { width: 56px; height: 56px; border-radius: 50%; background: var(--red); flex: none; }
  .brand__name { color: var(--green); font-size: 40px; }
  .person { position: absolute; left: 292px; top: 118px; }
  .person__name { color: var(--ink-green); font-size: 25px; line-height: 1.05; }
  .person__role { color: var(--red); font-size: 25px; line-height: 1.05; }
  .contact { position: absolute; left: 292px; top: 196px; list-style: none; font-size: 16px; line-height: 28px; }
  .contact__label { color: var(--red); }
  .contact__value { color: var(--ink-green); }
  .rule { position: absolute; left: 40px; right: 40px; height: 2px; background: var(--green); }
  .rule--top { top: 298px; }
  .rule--bottom { top: 362px; }
  .hours { position: absolute; left: 40px; top: 316px; font-size: 17px; color: var(--ink-green); white-space: nowrap; }
  .hours__label { color: var(--red); }
</style>
</head>
<body>

<section class="card card--back" aria-label="Card back">
  <svg class="card__art" viewBox="0 0 680 389" aria-hidden="false">
    <path d="M0 0 H680 V215 C590 120 400 52 0 30 Z" fill="var(--green)"/>
    <path d="M0 30 C400 52 590 120 680 215 V233 C590 138 400 68 0 44 Z" fill="var(--blue)"/>
    <rect x="0" y="44" width="0" height="0" fill="none"/>
    <g role="img" aria-label="Faint paw print decoration">
      <ellipse cx="110" cy="82" rx="30" ry="24" fill="var(--paw)"/>
    </g>
    <g role="img" aria-label="Faint paw print decoration">
      <ellipse cx="560" cy="185" rx="32" ry="26" fill="var(--paw)"/>
    </g>
    <g role="img" aria-label="Heart emblem with paw print">
      <path d="M340 78 C300 55 292 20 318 14 C332 11 340 22 340 28 C340 22 348 11 362 14 C388 20 380 55 340 78 Z" fill="var(--blue)" stroke="#fff" stroke-width="3"/>
    </g>
  </svg>
  <p class="back__name">HOBEL</p>
  <p class="back__tagline">“Making A Difference, One Pet At A Time.”</p>
  <p class="back__label">Our Websites</p>
  <p class="back__url back__url--one">www.KennoLoop.com/shelter40391-pets.html</p>
  <p class="back__url back__url--two">www.tailwick.com/shelters/vq216.html</p>
</section>

<section class="card card--front" aria-label="Card front">
  <svg class="card__art" viewBox="0 0 680 389">
    <path d="M0 0 H680 V225 C600 130 420 45 0 28 Z" fill="var(--green)"/>
    <path d="M0 28 C420 45 600 130 680 225 V245 C600 150 420 62 0 42 Z" fill="var(--blue)"/>
    <g role="img" aria-label="Heart emblem with paw print">
      <path d="M590 232 C530 205 500 150 530 132 C552 120 578 132 584 148 C594 130 624 118 644 134 C670 158 640 208 590 232 Z" fill="var(--blue)" stroke="#fff" stroke-width="4"/>
    </g>
  </svg>

  <div class="brand">
    <span class="brand__mark"></span>
    <span class="brand__name">HOBEL</span>
  </div>

  <div class="person">
    <p class="person__name">Maren Ostrowski</p>
    <p class="person__role">Co-Founder</p>
  </div>

  <ul class="contact">
    <li><span class="contact__label">Mobile:</span> <span class="contact__value">555 014 2287</span></li>
    <li><span class="contact__label">Email:</span> <span class="contact__value">maren.ost@hobelmail.com</span></li>
    <li><span class="contact__label">Address:</span> <span class="contact__value">1148 Harrow Ridge, Larkfield, TN 38999</span></li>
  </ul>

  <div class="rule rule--top"></div>
  <p class="hours"><span class="hours__label">Office Hours:</span> Monday - Sunday &nbsp;|&nbsp; Indoor hours vary so leave us a message.</p>
  <div class="rule rule--bottom"></div>
</section>

</body>
</html>
```